Verdant Bayline post card / handouts for customers

I am a New Orleans based meal prep company for health and fitness minded people who delivers executive chef quality food right to your door weekly. I am seeking a handout / postcard sized brochure that is straight and to the point. I need it to state step 1) go online step 2) order a la carte menu 3) deliver.

I will get into further detail with whomever I work with on specs.

My aesthetic is MODERN. I like LUMEVI.example aesthetic. Clean is key, Postcard design is 2 sided.

Industry/Entity Type

Fitness

Requirements
Must have
• Clean modern lines and photos. Bright and white!
Should not have
• Too busy, cluttered, too much info.

```html
<!DOCTYPE html>
<html lang="en">
<head>
<meta charset="utf-8">
<title>Verdant Bayline – Postcard, Front and Back</title>
<link rel="stylesheet" href="https://fonts.googleapis.com/css2?family=Fira+Sans+Condensed:wght@500;600&display=swap">
<style>
  :root {
    --page-bg: #ece9e4;
    --card-white: #ffffff;
    --ink: #1c1c1c;
    --stripe-a: #d9d9d9;
    --stripe-b: #ececec;
    --placeholder: #d6d6d6;
  }
  * { box-sizing: border-box; margin: 0; padding: 0; }
  html, body {
    width: 1200px; height: 1000px; overflow: hidden;
    background: var(--page-bg);
    font-family: "Fira Sans Condensed", "Arial Narrow", sans-serif;
    color: var(--ink);
  }
  .postcard {
    position: absolute; top: 150px;
    width: 480px; height: 700px;
    background: var(--card-white);
    box-shadow: 0 2px 10px rgba(0,0,0,.12);
  }
  .postcard--front { left: 90px; }
  .postcard--back { left: 630px; }
  .postcard__frame {
    position: absolute; inset: 14px;
    border: 2px solid var(--ink);
  }
  .stripe-band {
    position: absolute; left: 0; right: 0; height: 56px;
    background: repeating-linear-gradient(to bottom,
      var(--stripe-a) 0 4px, transparent 4px 9px,
      var(--stripe-b) 9px 13px, transparent 13px 18px);
  }
  .stripe-band--top { top: 8px; }
  .stripe-band--bottom { bottom: 8px; }

  /* Front */
  .brand-tag {
    position: absolute; top: 62px; left: 50%; transform: translateX(-50%);
    border: 2px solid var(--ink); background: var(--card-white);
    padding: 4px 12px; font-weight: 600; font-size: 20px; letter-spacing: 1px;
    white-space: nowrap;
  }
  .brand-leaf {
    position: absolute; top: 130px; left: 207px; width: 46px; height: 60px;
    border-radius: 50%; background: var(--placeholder);
  }
  .step { position: absolute; height: 80px; }
  .step--online { top: 248px; left: 70px; }
  .step--order { top: 352px; left: 96px; }
  .step--deliver { top: 458px; left: 120px; }
  .step__label {
    position: absolute; left: 22px; top: 0;
    border: 2px solid var(--ink); background: var(--card-white);
    padding: 8px 16px 8px 34px; font-weight: 600; font-size: 21px;
    letter-spacing: .5px; white-space: nowrap;
  }
  .step__number {
    position: absolute; left: 0; top: 30px; width: 44px; height: 44px;
    background: var(--ink); color: var(--card-white);
    font-weight: 600; font-size: 22px;
    display: flex; align-items: center; justify-content: center;
  }
  .cursor-icon { position: absolute; top: 236px; left: 302px; }
  .icon-slot { position: absolute; background: var(--placeholder); border-radius: 6px; }
  .icon-slot--bowl { top: 300px; left: 390px; width: 66px; height: 58px; border-radius: 0 0 33px 33px; }
  .icon-slot--van { top: 440px; left: 292px; width: 82px; height: 52px; }

  /* Back */
  .join-us {
    position: absolute; top: 512px; left: 0; right: 0; text-align: center;
    font-weight: 600; font-size: 19px; letter-spacing: 1.5px;
  }
  .social-row {
    position: absolute; top: 548px; left: 72px; width: 336px; height: 40px;
    display: flex; justify-content: space-between; align-items: center;
  }
  .social-row::before {
    content: ""; position: absolute; left: 0; right: 0; top: 50%;
    border-top: 2px solid var(--ink);
  }
  .social-row__slot {
    position: relative; width: 38px; height: 38px;
    background: var(--ink); border-radius: 8px;
  }
  .site-bar {
    position: absolute; top: 604px; left: 68px; right: 68px; height: 44px;
    background: var(--ink); color: var(--card-white);
    display: flex; align-items: center; justify-content: center;
    font-weight: 600; font-size: 20px; letter-spacing: 1.5px;
  }
</style>
</head>
<body>

<section class="postcard postcard--front" aria-label="Postcard front">
  <div class="stripe-band stripe-band--top"></div>
  <div class="stripe-band stripe-band--bottom"></div>
  <div class="postcard__frame"></div>

  <div class="brand-tag">VERDANT BAYLINE</div>
  <div class="brand-leaf" role="img" aria-label="Leaf emblem"></div>

  <svg class="cursor-icon" width="40" height="36" viewBox="0 0 40 36" aria-hidden="true">
    <path d="M4 4 L30 14 L20 17 L30 28 L26 31 L16 20 L10 28 Z" fill="none" stroke="#1c1c1c" stroke-width="2.5" stroke-linejoin="round"/>
  </svg>

  <div class="step step--online">
    <div class="step__label">GO ONLINE STEP</div>
    <div class="step__number">1</div>
  </div>
  <div class="icon-slot icon-slot--bowl" role="img" aria-label="Steaming bowl of soup icon"></div>

  <div class="step step--order">
    <div class="step__label">ORDER A LA CARTE MENU</div>
    <div class="step__number">2</div>
  </div>

  <div class="step step--deliver">
    <div class="step__label">DELIVER.</div>
    <div class="step__number">3</div>
  </div>
  <div class="icon-slot icon-slot--van" role="img" aria-label="Delivery van icon"></div>
</section>

<section class="postcard postcard--back" aria-label="Postcard back">
  <div class="stripe-band stripe-band--top"></div>
  <div class="stripe-band stripe-band--bottom"></div>
  <div class="postcard__frame"></div>

  <div class="join-us">JOIN US</div>
  <div class="social-row" aria-label="Social channels">
    <span class="social-row__slot"></span>
    <span class="social-row__slot"></span>
    <span class="social-row__slot"></span>
    <span class="social-row__slot"></span>
    <span class="social-row__slot"></span>
  </div>
  <div class="site-bar">WWW.YOURSITEHERE.COM</div>
</section>

</body>
</html>
```